Women's Online Clothing Boutique Needs Business Cards

I already have a logo that I would like to use. Some of the things that interest me is black business cards, foil embossed logo, glossy embossed logo, leopard print, no yellow font, rounded edges. I even like just a large logo on the front side with all of my information on the back side.

Contact Information for Business Card

https://silverheron.shopvenlo.com/
https://www.pagelink.net/thesilverheronboutique/
https://www.picfeed.net/thesilverheronboutique/
silverheronboutique@mailora.net

Requirements
Must have
• My Logo
Nice to have
• Leopard Print
Should not have
• No Yellow Font

```html
<!DOCTYPE html>
<html lang="en">
<head>
<meta charset="utf-8">
<title>The Silver Heron Boutique — Business Cards</title>
<link href="https://fonts.googleapis.com/css2?family=Questrial&family=Arimo:wght@400&display=swap" rel="stylesheet">
<style>
  :root {
    --backdrop: #c8babc;
    --card: #050707;
    --gold: #c9a224;
    --faint: #2a2a2a;
    --white: #ffffff;
    --text: #f2f2f2;
  }
  html, body {
    margin: 0;
    padding: 0;
    width: 1200px;
    height: 960px;
    overflow: hidden;
    background: var(--backdrop);
  }
  .canvas {
    position: relative;
    width: 1200px;
    height: 960px;
  }
  .card {
    position: absolute;
    width: 671px;
    height: 384px;
    background: var(--card);
    overflow: hidden;
  }
  .card--front { left: 258px; top: 48px; }
  .card--back  { left: 257px; top: 507px; }

  .brand {
    position: absolute;
    left: 0;
    right: 0;
    text-align: center;
    font-family: "Questrial", sans-serif;
    font-weight: 400;
    line-height: 1;
    margin: 0;
  }
  .brand__name { display: block; }
  .brand__sub { display: block; }

  .card--front .brand { top: 190px; color: var(--gold); }
  .card--front .brand__name { font-size: 54px; letter-spacing: -0.5px; }
  .card--front .brand__sub { font-size: 34px; margin-top: 10px; }

  .card--back .brand { top: 112px; color: var(--faint); }
  .card--back .brand__name { font-size: 30px; }
  .card--back .brand__sub { font-size: 19px; margin-top: 5px; }

  .stripes {
    position: absolute;
    top: 347px;
    width: 210px;
    height: 22px;
  }
  .stripes--left { left: 0; }
  .stripes--right { right: 0; }
  .stripe {
    position: absolute;
    left: 0;
    width: 100%;
    height: 2.5px;
  }
  .stripes--left .stripe { background: linear-gradient(to right, var(--white) 20%, rgba(255,255,255,0)); }
  .stripes--right .stripe { background: linear-gradient(to left, var(--white) 20%, rgba(255,255,255,0)); }
  .stripe:nth-child(1) { top: 0; }
  .stripe:nth-child(2) { top: 6px; }
  .stripe:nth-child(3) { top: 12px; }
  .stripe:nth-child(4) { top: 19px; }

  .contacts {
    position: absolute;
    left: 30px;
    top: 234px;
    margin: 0;
    padding: 0;
    list-style: none;
  }
  .contact {
    display: flex;
    align-items: center;
    height: 28.5px;
    font-family: "Arimo", sans-serif;
    font-size: 14.4px;
    color: var(--text);
  }
  .contact__icon {
    width: 22px;
    height: 22px;
    margin-right: 21px;
    flex: none;
  }
  .back-rule {
    position: absolute;
    left: 0;
    right: 0;
    top: 365px;
    height: 3px;
    background: var(--white);
  }
</style>
</head>
<body>
<div class="canvas">

  <section class="card card--front">
    <h1 class="brand">
      <span class="brand__name">The Silver Heron</span>
      <span class="brand__sub">Boutique</span>
    </h1>
    <div class="stripes stripes--left"><span class="stripe"></span><span class="stripe"></span><span class="stripe"></span><span class="stripe"></span></div>
    <div class="stripes stripes--right"><span class="stripe"></span><span class="stripe"></span><span class="stripe"></span><span class="stripe"></span></div>
  </section>

  <section class="card card--back">
    <p class="brand">
      <span class="brand__name">The Silver Heron</span>
      <span class="brand__sub">Boutique</span>
    </p>
    <ul class="contacts">
      <li class="contact">
        <svg class="contact__icon" viewBox="0 0 22 22" aria-hidden="true">
          <circle cx="11" cy="11" r="10" fill="none" stroke="#c9a224" stroke-width="1.4"/>
          <g fill="none" stroke="#ffffff" stroke-width="1">
            <circle cx="11" cy="11" r="6"/>
            <ellipse cx="11" cy="11" rx="2.6" ry="6"/>
            <line x1="5" y1="11" x2="17" y2="11"/>
            <line x1="6" y1="8" x2="16" y2="8"/>
            <line x1="6" y1="14" x2="16" y2="14"/>
          </g>
        </svg>
        <span>https://silverheron.shopvenlo.com/</span>
      </li>
      <li class="contact">
        <svg class="contact__icon" viewBox="0 0 22 22" aria-hidden="true"><circle cx="11" cy="11" r="10" fill="none" stroke="#c9a224" stroke-width="1.4"/></svg>
        <span>https://www.pagelink.net/thesilverheronboutique/</span>
      </li>
      <li class="contact">
        <svg class="contact__icon" viewBox="0 0 22 22" aria-hidden="true"><circle cx="11" cy="11" r="10" fill="none" stroke="#c9a224" stroke-width="1.4"/></svg>
        <span>https://www.picfeed.net/thesilverheronboutique/</span>
      </li>
      <li class="contact">
        <svg class="contact__icon" viewBox="0 0 22 22" aria-hidden="true"><circle cx="11" cy="11" r="10" fill="none" stroke="#c9a224" stroke-width="1.4"/></svg>
        <span>silverheronboutique@mailora.net</span>
      </li>
    </ul>
    <div class="back-rule"></div>
  </section>

</div>
</body>
</html>
```